RM Tomás Rivera (Business Card)

Hi designers, in this work, I'm looking for an sophisticated stylish, elegant and proffesional personal card. We have a laboratory of pathology automated, with equipments high quality.
In this web the designers, have created my business logo, the name is "RM Tomás Rivera"
In our lab, we principal work is to prepare the biopsies for further diagnostic of diseases like cancer, tumors, etc.
I need that the first face, only having my complete logo (Rm Tomás Rivera, Laboratorio de procesamiento Histologico)
The overleaf, could repeat the same logo, like water logo.
In this face, I need to say: My full data:

Técnico en Anatomía Patológica
Tomás Rivera Ibarra M.P 47203
Av. Paredes Luján 418 - 2do piso - Instituto Marbel.
Córdoba, Argentina
(0351) 154820937
rivera.tomas@correolab.example

with respect the colors of card, use your imagination, the original logo color is violet, I haven't chosen a color base for the card.

attached pictures are examples of cards I like your DESIGN.
Attached too, the original logo to my company.

the size of card are:
horizontal: 9cm
vertical: 5,5cm

any question that you have, not doubt to question me,
Hand to work!

Industry/Entity Type

Laboratory

Requirements
Must have
• designers sophisticated, not simples, like show the images attached

```html
<!DOCTYPE html>
<html lang="es">
<head>
<meta charset="utf-8">
<title>Tomás Rivera – Tarjeta personal</title>
<link rel="stylesheet" href="https://fonts.googleapis.com/css2?family=Ubuntu:wght@400;500;700&display=swap">
<style>
  :root{
    --page:#e9e9ec;
    --card-white:#ffffff;
    --ink-grey:#6d6d72;
    --ink-dark:#55555b;
    --violet:#8a2fa8;
    --violet-deep:#6a1d8a;
    --violet-light:#b04fd0;
    --magenta:#e0338f;
    --silver-top:#f2f2f3;
    --silver-bottom:#a9a9ad;
    --white:#ffffff;
  }
  *{margin:0;padding:0;box-sizing:border-box;}
  html,body{width:1200px;height:1000px;overflow:hidden;background:var(--page);}
  body{font-family:"Ubuntu",sans-serif;position:relative;}

  .card{
    position:absolute;left:240px;width:720px;height:440px;
    border-radius:6px;overflow:hidden;
    box-shadow:0 10px 30px rgba(0,0,0,.18);
  }
  .card--front{top:30px;background:var(--card-white);}
  .card--back{top:520px;background:linear-gradient(160deg,var(--silver-top),var(--silver-bottom));}

  .brand{position:absolute;display:flex;flex-direction:column;align-items:center;white-space:nowrap;}
  .brand__name{
    display:flex;align-items:center;gap:14px;
    font-weight:500;font-size:34px;letter-spacing:.18em;color:var(--violet);
  }
  .brand__mark{width:22px;height:22px;border-radius:50%;background:var(--violet);}
  .brand__rule{width:100%;height:1px;background:var(--ink-grey);margin:10px 0 8px;}
  .brand__tagline{font-size:17px;letter-spacing:.02em;color:var(--ink-grey);text-transform:uppercase;}

  .card--front .brand{left:50%;top:50%;transform:translate(-50%,-50%);}
  .card--back .brand{left:40px;top:26px;}
  .card--back .brand__name{font-size:24px;color:var(--white);text-shadow:0 1px 2px rgba(0,0,0,.2);}
  .card--back .brand__mark{width:16px;height:16px;background:var(--white);}
  .card--back .brand__rule{background:var(--white);margin:8px 0 6px;}
  .card--back .brand__tagline{font-size:13px;color:var(--white);text-shadow:0 1px 2px rgba(0,0,0,.2);}

  .swoosh{position:absolute;inset:0;width:720px;height:440px;}

  .holder{position:absolute;left:36px;top:146px;color:var(--white);white-space:nowrap;}
  .holder__name{font-weight:700;font-size:23px;text-shadow:0 1px 2px rgba(0,0,0,.3);}
  .holder__title{font-size:15px;margin-top:4px;margin-left:40px;color:var(--ink-dark);}

  .contact{position:absolute;right:24px;top:240px;color:var(--white);font-size:14px;white-space:nowrap;}
  .contact__row{display:flex;align-items:center;gap:10px;margin-bottom:14px;}
  .contact__row--phone{font-weight:700;font-size:16px;}
  .icon{width:22px;height:22px;flex:none;}

  .address{position:absolute;left:34px;top:350px;display:flex;gap:12px;color:var(--white);white-space:nowrap;}
  .address__lines{font-weight:700;font-size:16px;line-height:1.3;}
</style>
</head>
<body>

<section class="card card--front" aria-label="Frente de la tarjeta">
  <div class="brand">
    <div class="brand__name"><span class="brand__mark"></span>TOMÁS RIVERA</div>
    <div class="brand__rule"></div>
    <div class="brand__tagline">Laboratorio de procesamiento histológico</div>
  </div>
</section>

<section class="card card--back" aria-label="Dorso de la tarjeta">
  <svg class="swoosh" viewBox="0 0 720 440" aria-hidden="true">
    <defs>
      <linearGradient id="violetBand" x1="0" y1="1" x2="1" y2="0">
        <stop offset="0" stop-color="#6a1d8a"/>
        <stop offset="0.6" stop-color="#8a2fa8"/>
        <stop offset="1" stop-color="#b04fd0"/>
      </linearGradient>
    </defs>
    <path d="M0,330 C260,310 470,240 560,0 L720,0 L720,440 L0,440 Z" fill="url(#violetBand)"/>
    <path d="M0,314 C250,294 450,226 536,0" fill="none" stroke="#ffffff" stroke-opacity=".55" stroke-width="3"/>
    <path d="M0,344 C270,324 486,252 580,0" fill="none" stroke="#e0338f" stroke-width="2"/>
    <path d="M0,356 C280,336 500,262 596,0" fill="none" stroke="#ffffff" stroke-opacity=".25" stroke-width="6"/>
  </svg>

  <div class="brand">
    <div class="brand__name"><span class="brand__mark"></span>TOMÁS RIVERA</div>
    <div class="brand__rule"></div>
    <div class="brand__tagline">Laboratorio de procesamiento histológico</div>
  </div>

  <div class="holder">
    <div class="holder__name">Tomás Rivera Ibarra M.P 47203</div>
    <div class="holder__title">Técnico en Anatomía Patológica</div>
  </div>

  <div class="contact">
    <div class="contact__row contact__row--phone">
      <svg class="icon" viewBox="0 0 24 24" aria-hidden="true"><rect x="6" y="1" width="12" height="22" rx="2" fill="none" stroke="#fff" stroke-width="2"/><circle cx="12" cy="19" r="1.3" fill="#fff"/></svg>
      (0351) 154820937
    </div>
    <div class="contact__row">
      <svg class="icon" viewBox="0 0 24 24" aria-hidden="true"><rect x="1" y="5" width="22" height="14" fill="#fff"/><path d="M1,5 L12,13 L23,5" fill="none" stroke="#8a2fa8" stroke-width="1.6"/></svg>
      rivera.tomas@correolab.example
    </div>
  </div>

  <div class="address">
    <svg class="icon" viewBox="0 0 24 24" aria-hidden="true"><path d="M12,2 L23,12 L19,12 L19,22 L5,22 L5,12 L1,12 Z" fill="#fff"/></svg>
    <div class="address__lines">
      Av. Paredes Luján 418 - 2do piso<br>
      Instituto Marbel.<br>
      Córdoba, Argentina
    </div>
  </div>
</section>

</body>
</html>
```